Need a Modern WIX Website design

Need help designing a modern WIX website. I already started building on studio.plovex.com but I am not a designer and would like a more modern, update aesthetic look. This is not an e-commerce site. Just a website portraying our company, posting what products we offer, contact, about us, services. Logo is already on the studio.plovex version with some content. Need a designer with vision, and ingenuity to set it apart change it a little and make it stand out. Please look at the current site for redesign and/or ideas https://norvatradeco.plovexsite.com/website
also need the design to be connected to our google domain www.nvt.trade

Please feel free to ask as many questions as possible

Target Market(s)

Tire repair shops, Tire stores, mechanic shops, tire replacement franchises, wheel and rim stores

Industry/Entity Type

we are wholesalers, B2B ..sell tire repair materials, tire hand tools, machinery, chemicals, wheel lug nuts, wheel accessories

Coding

Coded - Design and coding required

Number of Pages Required

5+ page

Font styles to use
Other font styles liked:
• Let designer choose

Colors

Designer to choose colors to be used in the design.

Requirements
Must have
• modern design layout, videos, high quality pictures, different ideas for pages (Home, shop, about, products, services, contact, faq, meet the team) translatable english to spanish
Nice to have
• would like to have an up to date modern look, interactive, easy to navigate,
Should not have
• not be hard to navigate for our customers

```html
<!DOCTYPE html>
<html lang="en">
<head>
<meta charset="utf-8">
<title>Norva Trade Co — Tire Repair Supplier</title>
<link rel="stylesheet" href="https://fonts.googleapis.com/css2?family=Saira+Condensed:wght@500;600;700;800&family=Lato:wght@400;700&display=swap">
<style>
:root{
  --red:#e23a3e;
  --red-deep:#c92c31;
  --ink:#141414;
  --dark:#1b1b1b;
  --paper:#f4f4f4;
  --white:#ffffff;
  --grey:#555;
  --line:#2e2e2e;
}
*{margin:0;padding:0;box-sizing:border-box}
html,body{width:1200px;height:4451px;overflow:hidden}
body{position:relative;background:var(--white);font-family:"Lato",sans-serif;color:var(--ink)}
.abs{position:absolute}
.head{font-family:"Saira Condensed",sans-serif;font-weight:700;text-transform:uppercase}
/* header */
.brand{left:0;width:1200px;top:22px;text-align:center;font-family:"Saira Condensed",sans-serif;font-weight:800;font-size:44px;line-height:48px;color:var(--ink);letter-spacing:2px}
.brand small{display:block;font-size:11px;line-height:16px;font-weight:600;letter-spacing:3px;color:var(--grey)}
.navline{left:66px;width:1068px;top:104px;height:1px;background:#ddd}
.nav{top:122px;left:0;width:1200px;display:flex;justify-content:center;gap:34px;font-size:15px;text-transform:uppercase}
.nav a{color:var(--ink);text-decoration:none}
.nav a.on{color:var(--red)}
/* hero */
.hero-bg{top:0;left:0;width:1200px;height:1310px;background:var(--paper);z-index:-2}
.word{top:190px;left:0;width:1200px;text-align:center;font-family:"Saira Condensed",sans-serif;font-weight:800;font-size:230px;line-height:1;letter-spacing:64px;padding-left:64px;color:var(--ink)}
.car{left:270px;top:270px;width:660px;height:300px;background:radial-gradient(ellipse 50% 46% at 50% 52%,#e8c21c 0%,#c9a214 48%,rgba(60,60,60,.55) 80%,rgba(244,244,244,0) 100%)}
.mech{left:66px;top:682px;width:397px;height:544px;background:linear-gradient(160deg,#8d8d8d,#3d3d3d)}
.kicker{left:511px;top:800px;color:var(--red);font-size:24px;font-weight:600}
.h1{left:511px;top:834px;color:var(--white);font-size:52px;line-height:58px}
.lead{left:511px;top:988px;width:620px;color:#e8e8e8;font-size:19px;line-height:33px}
/* services */
.svc-title{top:1372px;width:1200px;text-align:center;color:var(--white);font-size:54px}
.card{top:1475px;width:342px;height:350px}
.card.a{left:66px;background:linear-gradient(135deg,#d9c1a8,#6f6a66)}
.card.b{left:430px;background:#111;color:#fff;text-align:center;padding:110px 20px 0}
.card.c{left:793px;background:linear-gradient(180deg,#e8e8e8,#2f4368)}
.card.b h3{color:var(--red);font-size:24px;margin-bottom:14px}
.card.b p{font-size:15px;line-height:25px;color:#ddd}
.arrow{top:1630px;width:42px;height:42px;border-radius:50%;background:#fff;border:1px solid #ccc;display:flex;align-items:center;justify-content:center}
/* products */
.feat{top:1888px;width:1200px;text-align:center;font-size:54px}
.prod{width:251px}
.prod .img{height:277px;background:var(--paper);display:flex;align-items:center;justify-content:center}
.prod .img i{display:block;width:150px;height:90px;border-radius:14px;background:linear-gradient(180deg,#e6e6e6,#8d8d8d)}
.prod .img.hover{background:#e25a5d}
.prod .img.hover span{color:#fff;text-decoration:underline;font-size:15px}
.prod h4{margin-top:24px;font-size:21px;font-family:"Saira Condensed",sans-serif;font-weight:700;text-transform:uppercase}
.prod p{font-size:15px;color:#444;margin-top:4px}
/* dark */
.dark{top:2806px;left:0;width:1200px;height:1176px;background:var(--dark)}
.sec-t{width:1200px;text-align:center;color:#fff;font-size:52px;line-height:56px}
.sec-s{width:1200px;text-align:center;color:#ddd;font-size:17px;letter-spacing:5px;text-transform:uppercase}
.logo-box{width:245px;height:117px;border:1px solid var(--line);display:flex;align-items:center;justify-content:center}
.logo-lab{width:245px;text-align:center;color:#fff;font-family:"Saira Condensed",sans-serif;font-weight:600;font-size:20px;text-transform:uppercase}
.emp{top:3500px;width:520px;height:432px}
.emp .name{position:absolute;bottom:70px;width:100%;text-align:center;color:#fff;font-size:30px}
.emp .role{position:absolute;bottom:52px;width:100%;text-align:center;color:#eee;font-size:14px;text-transform:uppercase}
/* footer */
.foot{top:3981px;left:0;width:1200px;height:470px;background:var(--red)}
.f-brand{left:66px;top:4040px;color:#fff;font-family:"Saira Condensed",sans-serif;font-weight:800;font-size:48px;line-height:56px;letter-spacing:2px}
.f-text{left:66px;top:4156px;width:320px;color:#fff;font-size:16px;line-height:25px}
.social{top:4287px;width:40px;height:40px;border:2px solid #fff;border-radius:50%}
.f-h{top:4040px;color:#fff;font-size:25px}
.f-item{left:547px;color:#fff;font-size:16px;line-height:23px}
.f-ico{left:512px}
.email{left:867px;top:4100px;width:268px;height:48px;background:var(--red-deep);border:1px solid #e87b7d;color:#f2b0b1;font-size:14px;padding:14px 14px}
.sub{left:867px;top:4158px;width:268px;height:50px;background:#fff;color:var(--ink);font-size:16px;text-align:center;line-height:50px}
.copy{top:4395px;width:1200px;text-align:center;color:#fff;font-size:14px;text-transform:uppercase}
</style>
</head>
<body>
<div class="abs hero-bg"></div>

<header>
  <div class="abs brand">NORVA TRADE CO<small>SPECIALIZING IN TIRE SOLUTIONS</small></div>
  <div class="abs navline"></div>
  <nav class="abs nav">
    <a class="on">Home</a><a>Shop</a><a>About</a><a>Products</a><a>Services</a><a>Contact</a><a>FAQ</a><a>Meet the Team</a><a>Wheel Lug Nuts &amp; Bolts</a>
  </nav>
</header>

<section>
  <svg class="abs" style="left:0;top:470px" width="1200" height="840" viewBox="0 0 1200 840">
    <polygon points="1200,0 1200,840 0,840 0,430" fill="#141414"/>
  </svg>
  <div class="abs word">NORVA</div>
  <div class="abs car" role="img" aria-label="Photo of a yellow sports coupe in three-quarter front view"></div>
  <div class="abs mech" role="img" aria-label="Photo of a mechanic fitting a tire onto a car wheel"></div>
  <div class="abs head kicker">Your One Stop</div>
  <h1 class="abs head h1">Tire Repair Supplier<br>In New York</h1>
  <p class="abs lead">At Norva Trade Co we make sure to offer our clients the best selection of tire repair products, tools and machinery as well as provide them with superb customer service. Our staff works with our customers to find exactly the right part they need for the right price.</p>
</section>

<section>
  <svg class="abs" style="left:0;top:1309px" width="1200" height="582" viewBox="0 0 1200 582">
    <rect width="1200" height="582" fill="#e23a3e"/>
    <polygon points="0,122 0,582 1200,582 1200,580 430,290" fill="#fff"/>
    <polygon points="0,520 1200,582 0,582" fill="#fff"/>
    <polygon points="700,400 1200,470 1200,582" fill="#e23a3e"/>
  </svg>
  <h2 class="abs head svc-title">Our Services</h2>
  <div class="abs card a" role="img" aria-label="Photo of a team stacking hands together in an office"></div>
  <div class="abs card b"><h3 class="head">Innovation</h3><p>We keep innovating to improve the experience for customers and everyone who uses our spaces.</p></div>
  <div class="abs card c" role="img" aria-label="Photo of a businessman raising arms in celebration"></div>
  <div class="abs arrow" style="left:12px"><svg width="12" height="12" viewBox="0 0 12 12"><path d="M8 1 3 6l5 5" stroke="#222" stroke-width="1.6" fill="none"/></svg></div>
  <div class="abs arrow" style="left:1146px"><svg width="12" height="12" viewBox="0 0 12 12"><path d="M4 1l5 5-5 5" stroke="#222" stroke-width="1.6" fill="none"/></svg></div>
</section>

<section>
  <h2 class="abs head feat">Featured Products</h2>
  <div class="abs prod" style="left:66px;top:1977px"><div class="img" role="img" aria-label="Photo of a chrome lug nut"><i></i></div><h4>Factory Style</h4><p>Heavy Duty Trucks (7/8)</p></div>
  <div class="abs prod" style="left:338px;top:1977px"><div class="img hover"><span>VIEW DETAILS</span></div><h4>Spline Lug Nut</h4><p>Adapter - Truck Spline</p></div>
  <div class="abs prod" style="left:611px;top:1977px"><div class="img" role="img" aria-label="Photo of a spline lug nut adapter"><i style="height:40px;width:170px"></i></div><h4>Spline Lug Nut</h4><p>Adapter - Truck Spline</p></div>
  <div class="abs prod" style="left:883px;top:1977px"><div class="img" role="img" aria-label="Photo of a slim spline adapter"><i style="height:34px;width:190px"></i></div><h4>Kozan</h4><p>Adapter - Car Spline</p></div>
  <div class="abs prod" style="left:66px;top:2375px"><div class="img" role="img" aria-label="Photo of a brass air coupler"><i style="background:linear-gradient(180deg,#e2b64a,#7d5a12);height:70px"></i></div><h4>1/4" FNPT Female</h4><p>M-Style Quick-Change Coupler</p></div>
  <div class="abs prod" style="left:338px;top:2375px"><div class="img" role="img" aria-label="Photo of a can of vulcanizing fluid"><i style="width:100px;height:150px;border-radius:30px 30px 10px 10px"></i></div><h4>CV-12 Cold</h4><p>Vulcanizing Fluid</p></div>
  <div class="abs prod" style="left:611px;top:2375px"><div class="img" role="img" aria-label="Photo of chrome lug nuts with washer"><i></i></div><h4>Factory Style</h4><p>Lug - Import w/Washer</p></div>
  <div class="abs prod" style="left:883px;top:2375px"><div class="img" role="img" aria-label="Photo of a digital tire inflator with pistol grip"><i style="width:70px;height:150px;background:linear-gradient(180deg,#b8242a,#222)"></i></div><h4>Pro Digital Tire</h4><p>Inflator/Pressure Pistol Grip...</p></div>
</section>

<section>
  <div class="abs dark"></div>
  <svg class="abs" style="left:0;top:3420px" width="1200" height="562" viewBox="0 0 1200 562">
    <polygon points="0,430 1200,60 1200,0 600,140" fill="#fff"/>
    <polygon points="0,360 1200,140 1200,400 0,562" fill="#e23a3e"/>
  </svg>
  <h2 class="abs head sec-t" style="top:2842px">Brands</h2>
  <p class="abs sec-s" style="top:2912px">Who we work with</p>

  <div class="abs logo-box" style="left:66px;top:2957px"><svg width="80" height="80"><polygon points="40,4 74,22 74,58 40,76 6,58 6,22" fill="none" stroke="#bbb" stroke-width="2"/></svg></div>
  <div class="abs logo-box" style="left:338px;top:2957px"><svg width="80" height="80"><circle cx="40" cy="40" r="34" fill="none" stroke="#bbb" stroke-width="2"/><circle cx="40" cy="40" r="24" fill="none" stroke="#bbb" stroke-width="2"/></svg></div>
  <div class="abs logo-box" style="left:615px;top:2957px"><svg width="80" height="80"><polygon points="8,40 40,8 72,40 40,72" fill="none" stroke="#bbb" stroke-width="2"/></svg></div>
  <div class="abs logo-box" style="left:889px;top:2957px"><svg width="80" height="80"><circle cx="40" cy="40" r="34" fill="none" stroke="#bbb" stroke-width="2"/><circle cx="40" cy="40" r="26" fill="none" stroke="#bbb" stroke-width="2"/><circle cx="40" cy="40" r="18" fill="none" stroke="#bbb" stroke-width="2"/></svg></div>
  <div class="abs logo-lab" style="left:66px;top:3085px">Kestrel Patch</div>
  <div class="abs logo-lab" style="left:338px;top:3085px">Harbor Line Inc</div>
  <div class="abs logo-lab" style="left:615px;top:3085px">Delvan Industries</div>
  <div class="abs logo-lab" style="left:889px;top:3085px">Orrin Wade Industries</div>

  <div class="abs logo-box" style="left:66px;top:3143px"><svg width="80" height="80"><circle cx="40" cy="40" r="32" fill="none" stroke="#bbb" stroke-width="2"/></svg></div>
  <div class="abs logo-box" style="left:338px;top:3143px"><svg width="80" height="80"><rect x="12" y="12" width="56" height="56" fill="none" stroke="#bbb" stroke-width="2"/></svg></div>
  <div class="abs logo-box" style="left:615px;top:3143px"><svg width="80" height="80"><polygon points="8,12 72,12 40,70" fill="none" stroke="#bbb" stroke-width="2"/></svg></div>
  <div class="abs logo-box" style="left:889px;top:3143px"><svg width="80" height="80"><polygon points="40,4 74,22 74,58 40,76 6,58 6,22" fill="none" stroke="#bbb" stroke-width="2"/><circle cx="40" cy="40" r="14" fill="none" stroke="#bbb" stroke-width="2"/></svg></div>
  <div class="abs logo-lab" style="left:66px;top:3272px">Brightel Solutions</div>
  <div class="abs logo-lab" style="left:338px;top:3272px">Tarvel</div>
  <div class="abs logo-lab" style="left:615px;top:3272px">Ridgeway Weld</div>
  <div class="abs logo-lab" style="left:889px;top:3272px">Corbrand Tools</div>

  <h2 class="abs head sec-t" style="top:3370px">Employees</h2>
  <p class="abs sec-s" style="top:3440px">The people who make the difference</p>
  <div class="abs emp" style="left:66px;background:linear-gradient(180deg,#6b6b6b,#2c2c2c)" role="img" aria-label="Portrait photo of the company president"><div class="head name">Daniel Ortega</div><div class="role">President</div></div>
  <div class="abs emp" style="left:615px;background:linear-gradient(180deg,#b48a5a,#3e4a32)" role="img" aria-label="Portrait photo of the executive administrator"><div class="head name">Laura Brennan</div><div class="role">Executive Administrator</div></div>
</section>

<footer>
  <div class="abs foot"></div>
  <div class="abs f-brand">NORVA TRADE CO</div>
  <p class="abs f-text">At Norva Trade Co we make sure to offer our clients the best selection of tire repair products, tools and machinery as well as...</p>
  <div class="abs social" style="left:66px"></div>
  <div class="abs social" style="left:122px"></div>
  <div class="abs social" style="left:178px"></div>

  <h3 class="abs head f-h" style="left:501px">Contact Us</h3>
  <svg class="abs f-ico" style="top:4122px" width="14" height="20" viewBox="0 0 14 20"><path d="M7 0a7 7 0 0 0-7 7c0 5 7 13 7 13s7-8 7-13a7 7 0 0 0-7-7zm0 10a3 3 0 1 1 0-6 3 3 0 0 1 0 6z" fill="#fff"/></svg>
  <p class="abs f-item" style="top:4110px">214 Harlow Avenue<br>Brookfield, NY 10455</p>
  <svg class="abs f-ico" style="top:4193px" width="16" height="16" viewBox="0 0 16 16"><path d="M3 1l3 3-2 2c1 2 4 5 6 6l2-2 3 3-2 2C7 15 1 9 1 3z" fill="#fff"/></svg>
  <p class="abs f-item" style="top:4190px">555-204-7719</p>
  <svg class="abs f-ico" style="top:4265px" width="16" height="12" viewBox="0 0 16 12"><rect width="16" height="12" fill="#fff"/><path d="M0 0l8 6 8-6" stroke="#e23a3e" fill="none"/></svg>
  <p class="abs f-item" style="top:4261px">hello@nvt.trade</p>

  <h3 class="abs head f-h" style="left:867px">Newsletter</h3>
  <div class="abs email">Enter Email</div>
  <div class="abs sub">SUBSCRIBE</div>
  <p class="abs copy">Copyright © 2022 Norva Trade Co. All rights reserved.</p>
</footer>
</body>
</html>
```